Updating of Business cards

We are looking to update our current business cards.

Size to be 85 mm x 55 mm - can be double sided

Please find attached current designs and a copy of our logo.

We would like the cards to have on them some of the photos we have had taken.

To include:

Name, Company address, phone number, email address, website address
Link to our FaceBook page and Instagram (We do have Twitter but not used very often)

Please note we will need one version of the cards to include:
Name, Position, Company address, phone number, Mobile, personal email address, BrightForge email address, website address

We would like the cards to say something along the lines of "Metal laser cutting, folding & fabrication"

Please visit our website www.brightforge-example.co.uk to find out more about what we do.

We will need the files in a format where we can add the names etc onto the Cards. We can open ai. files.

Thank you in advance :)

```html
<!DOCTYPE html>
<html lang="en">
<head>
<meta charset="utf-8">
<title>BrightForge Business Cards</title>
<link rel="stylesheet" href="https://fonts.googleapis.com/css2?family=Arimo:wght@400;700&display=swap">
<style>
  :root {
    --bg: #e9e6e1;
    --card-dark: #3b3b3c;
    --orange: #f5a11c;
    --white: #ffffff;
    --grey-light: #c9c9c9;
    --grey-mid: #9a9a9a;
    --photo-dark: #2c2a2a;
    --photo-red: #8a2f30;
  }
  * { margin: 0; padding: 0; box-sizing: border-box; }
  html, body {
    width: 1200px; height: 900px; overflow: hidden;
    background: var(--bg);
    font-family: "Arimo", Arial, sans-serif;
  }
  .sheet {
    position: relative; width: 1200px; height: 900px;
  }
  .card {
    position: absolute; left: 280px; width: 640px; height: 414px;
    overflow: hidden;
    box-shadow: 0 6px 18px rgba(0,0,0,0.18);
  }
  .card-front { top: 24px; background: var(--photo-dark); }
  .card-back { top: 462px; background: var(--card-dark); }

  /* front */
  .front-photo {
    position: absolute; inset: 0 0 74px 0;
    background:
      linear-gradient(160deg, rgba(20,20,20,0.85) 0%, rgba(20,20,20,0.2) 35%, rgba(20,20,20,0) 60%),
      linear-gradient(120deg, var(--photo-dark) 0%, #5a2526 30%, var(--photo-red) 55%, #6e2a2a 75%, #3a3535 100%);
  }
  .front-brand {
    position: absolute; left: 44px; top: 150px;
    color: var(--white); font-weight: 700; font-size: 72px; letter-spacing: -1px;
  }
  .front-tagline {
    position: absolute; left: 48px; top: 236px;
    color: var(--white); font-weight: 700; font-size: 22px;
  }
  .front-band {
    position: absolute; left: 0; right: 0; top: 340px; height: 26px;
    background: var(--orange);
    color: var(--white); font-size: 14px; text-align: center; line-height: 26px;
  }
  .front-strip { position: absolute; left: 0; right: 0; top: 366px; height: 28px; background: #4a3d3a; }
  .front-edge { position: absolute; left: 0; right: 0; bottom: 0; height: 20px; background: var(--orange); }

  /* back */
  .back-brand {
    position: absolute; left: 40px; top: 92px;
    color: var(--orange); font-weight: 700; font-size: 46px; letter-spacing: -0.5px;
  }
  .back-tagline {
    position: absolute; left: 42px; top: 146px;
    color: var(--orange); font-size: 15px;
  }
  .person {
    position: absolute; right: 40px; top: 48px; text-align: right;
  }
  .person-name { color: var(--white); font-size: 34px; }
  .person-role { color: var(--orange); font-size: 13px; margin-top: 6px; }
  .person-company { color: var(--grey-light); font-size: 13px; margin-top: 4px; }

  .contact {
    position: absolute; left: 40px; top: 222px; color: var(--white); font-size: 14px; line-height: 19px;
  }
  .contact-row { display: flex; align-items: center; gap: 10px; }
  .contact-row svg { width: 16px; height: 16px; flex: none; }
  .contact-indent { padding-left: 26px; }

  .social {
    position: absolute; right: 40px; top: 196px; color: var(--white); font-size: 14px; line-height: 26px; text-align: right;
  }
  .social-row { display: flex; justify-content: flex-end; align-items: center; gap: 10px; }
  .social-mark { width: 14px; height: 14px; background: var(--orange); }

  .swoosh { position: absolute; left: 0; bottom: 0; width: 640px; height: 170px; }
</style>
</head>
<body>
<div class="sheet">

  <section class="card card-front">
    <div class="front-photo" role="img" aria-label="Photo of a red press brake folding machine in the workshop"></div>
    <div class="front-brand">BrightForge</div>
    <div class="front-tagline">Metal laser cutting, folding &amp; fabrication</div>
    <div class="front-band">www.brightforge-example.co.uk</div>
    <div class="front-strip"></div>
    <div class="front-edge"></div>
  </section>

  <section class="card card-back">
    <div class="back-brand">BrightForge</div>
    <div class="back-tagline">Metal laser cutting, folding &amp; fabrication</div>

    <div class="person">
      <div class="person-name">Daniel Hart</div>
      <div class="person-role">National Sales Manager</div>
      <div class="person-company">BrightForge Ltd</div>
    </div>

    <div class="contact">
      <div class="contact-indent">Kestrel Way Industrial Estate</div>
      <div class="contact-indent">Penwith, Truro TR9 4QX</div>
      <div class="contact-row">
        <svg viewBox="0 0 16 16"><path d="M4 1.5 6.5 4 5 6c.8 2 2.5 3.9 5 5l2-1.5 2.5 2.5-2 2.5C7 14 2 9 1.5 3.5Z" fill="var(--orange)"/></svg>
        <span>01632 960418</span>
      </div>
      <div class="contact-row">
        <svg viewBox="0 0 16 16"><rect x="1" y="3.5" width="14" height="9" fill="none" stroke="var(--orange)" stroke-width="1.5"/><path d="M1 3.5 8 9l7-5.5" fill="none" stroke="var(--orange)" stroke-width="1.5"/></svg>
        <span>daniel@brightforge-example.co.uk</span>
      </div>
      <div class="contact-indent">sales@brightforge-example.co.uk</div>
      <div class="contact-row">
        <svg viewBox="0 0 16 16"><circle cx="8" cy="8" r="6.5" fill="none" stroke="var(--orange)" stroke-width="1.3"/><ellipse cx="8" cy="8" rx="3" ry="6.5" fill="none" stroke="var(--orange)" stroke-width="1.1"/><path d="M1.5 8h13M2.5 5h11M2.5 11h11" stroke="var(--orange)" stroke-width="1"/></svg>
        <span>www.brightforge-example.co.uk</span>
      </div>
    </div>

    <div class="social">
      <div class="social-row"><span>BrightForgeCornwall</span><span class="social-mark"></span></div>
      <div class="social-row"><span>@bright_forge_uk</span><span class="social-mark"></span></div>
    </div>

    <svg class="swoosh" viewBox="0 0 640 170" preserveAspectRatio="none" aria-hidden="true">
      <path d="M0 170 C200 150 420 110 640 20 L640 50 C440 130 240 165 60 170 Z" fill="var(--grey-mid)"/>
      <path d="M0 170 C220 160 440 130 640 60 L640 170 Z" fill="var(--orange)"/>
      <path d="M30 170 C250 165 450 140 640 85 L640 170 Z" fill="var(--card-dark)"/>
      <path d="M0 170 C160 140 260 120 330 115 C230 135 120 160 40 170 Z" fill="var(--grey-light)"/>
    </svg>
  </section>

</div>
</body>
</html>
```